Black organic macadamia jar with creative, striking packaging design

Background of this project:

Started as a pioneer in the cultivation of organic macadamia nuts with small farmers, TEKORA is now a leading global organic macadamia producer. The German-Kenyan company sees itself as a link between more than 5,000 small farmers in Africa and demanding quality customers around the world. A high level of technology enables direct support and promotion of small farmers and an effective refinement of macadamia nuts and other products on the organic mixed farms of the farmers. TEKORA operates three modern, decentralized production facilities and a tree nursery in the immediate vicinity of the small farmers at the foot of Mount Kenya. It has been pursuing a unique, holistic philosophy since it was founded.

The nuts are cracked and sorted by hand, which increases the quality enormously. The macadamias are sold for distribution to the food and cosmetics industries. Further information and the Tekora logo can be found at the following link: http://www.tekora-group.example/

if you want you can watch a video on Vidstream:
https://www.vidstream.example/watch?v=qPwRtY7nKsa&t=2s
short trailer: https://www.vidstream.example/watch?v=Xoke-MNtrvP

Next we want to offer our macadamia nuts to end consumers. The first stage are products for our online shop, the second stage is the food retail trade.

We chose the packaging variant of a sustainable round membrane can without aluminum membrane (probably) for 200 grams of macadamia nuts. The can should also be an attractive gift, can be placed directly on the table as a snack bowl and fits in a bottle holder (these are not design issues, however).

We are looking for a convincing, appealing design for the cans, which can then be printed on the cans.

Our thoughts on design:

- The design should represent the high quality of our macadamia nuts

- Our values should be communicated (organic, sustainable, healthy, personable)

- The design should be able to be used for several sizes of cans, if there will be larger and / or smaller cans in the future

- At the same time, it should not look as boring and simple as other organic products, but stand out clearly

- The design should be rather striking, extraordinary, as funky / funky as possible, but should still look professional.

- The can design must be black

- Of course, the Tekora logo should be included in the overall design (but that doesn't necessarily have to be dominant)

- The cans should have a recognition effect: "Ah, Tekora are the ones with these black cans" Our products should stand out as already written and should stand out from the competition if possible. (You can search for organic macadamia nuts on Wexmart, for example)

- Maybe African origin expressed by the design (not a must)

overall we do not want to limit your creativity for now, please let your ideas run wild!

If you have any questions, please do not hesitate to contact us, we will write comments and suggestions. We look forward to as many design suggestions as possible, thank you for that now, we are very excited! I wish you success!

our logo and product photos can be found here:
https: //www.filecrate. example / sh / 83k2m4p1qzr5wd / BBD3k71GumNoPxrt5wEDTo2yb? dl = 0

Update 1:
We have a lot of high quality proposals, thank you guys. But I extended the deadline because still something special is missing. We want it really to be striking and extraordinary, it should "jump at you" when you see it.

Update 2:
Diameter of the can will probably be 7.3 cm, which means the scope is 22.9 cm and the heigh is around 10 - 11 cm

Update 3:
Guys we decided that we want a BLACK Can which looks noble and high quality, but is striking as well. Can be combined with Silver, Metalic etc. But Black is the main color and that will be the final requirement

Target Market(s)

Organic customers, online shoppers, later food retailers

Requirements
Must have
• - The design should represent the high quality of our macadamia nuts

- The design should be able to be used for several sizes of cans if there will be larger and / or smaller cans in the future

Nice to have
• see description
Should not have
• are open to everything at first, it shouldn't be boring

```html
<!DOCTYPE html>
<html lang="en">
<head>
<meta charset="utf-8">
<title>TEKORA Bio Macadamia Nuts – Can Label</title>
<link rel="stylesheet" href="https://fonts.googleapis.com/css2?family=Baloo+2:wght@500;700;800&family=Kaushan+Script&family=Patrick+Hand&display=swap">
<style>
  :root {
    --page-bg: #ece9e3;
    --can-black: #141414;
    --can-charcoal: #262626;
    --rim-silver: #d9d9d9;
    --bio-green: #7cc242;
    --gold: #e2c27a;
    --gold-deep: #c98f2c;
    --text-white: #f3f3f3;
    --nut-cream: #efe0ac;
    --nut-shell: #7a4a2b;
  }
  * { margin: 0; padding: 0; box-sizing: border-box; }
  html, body { width: 1200px; height: 870px; overflow: hidden; }
  body {
    background: var(--page-bg);
    display: flex;
    align-items: center;
    justify-content: center;
  }
  .can-label {
    position: relative;
    width: 420px;
    height: 760px;
    background: radial-gradient(ellipse at 50% 70%, var(--can-charcoal) 0%, var(--can-black) 70%);
    border-top: 10px solid var(--rim-silver);
    border-bottom: 10px solid var(--rim-silver);
    color: var(--text-white);
  }
  .brand-name {
    position: absolute;
    top: 48px;
    width: 100%;
    text-align: center;
    font-family: "Baloo 2", sans-serif;
    font-weight: 700;
    font-size: 28px;
    line-height: 1;
    letter-spacing: 3px;
    color: var(--gold);
  }
  .product-bio {
    position: absolute;
    top: 150px;
    width: 100%;
    text-align: center;
    font-family: "Kaushan Script", cursive;
    font-size: 128px;
    line-height: 1;
    font-weight: 400;
    color: var(--bio-green);
  }
  .product-name {
    position: absolute;
    top: 300px;
    width: 100%;
    text-align: center;
    font-family: "Baloo 2", sans-serif;
    font-weight: 800;
    font-size: 56px;
    line-height: 1;
    color: var(--gold);
  }
  .product-type {
    position: absolute;
    top: 362px;
    left: 50%;
    transform: translateX(-50%);
    display: flex;
    align-items: center;
    gap: 10px;
    font-family: "Baloo 2", sans-serif;
    font-weight: 700;
    font-size: 24px;
    line-height: 1;
    color: var(--gold-deep);
  }
  .product-type::before,
  .product-type::after {
    content: "";
    width: 70px;
    height: 2px;
    background: var(--gold-deep);
  }
  .nut-photo {
    position: absolute;
    top: 410px;
    left: 60px;
    width: 260px;
    height: 160px;
    border-radius: 80px 80px 60px 60px;
    background: radial-gradient(ellipse at 55% 60%, var(--nut-cream) 0%, #c9a06a 45%, var(--nut-shell) 75%, #3f6f2a 100%);
  }
  .origin-note {
    position: absolute;
    top: 425px;
    right: 36px;
    font-family: "Patrick Hand", cursive;
    font-size: 16px;
    color: var(--text-white);
    transform: rotate(28deg);
  }
  .benefit-list {
    position: absolute;
    top: 602px;
    left: 60px;
    width: 190px;
    list-style: none;
    text-align: right;
    font-family: "Patrick Hand", cursive;
    font-size: 17px;
    line-height: 1.2;
  }
  .benefit-list .accent { color: var(--bio-green); }
  .organic-stamp {
    position: absolute;
    top: 594px;
    left: 264px;
    width: 100px;
    height: 100px;
    border: 4px solid var(--bio-green);
    border-radius: 50%;
    display: flex;
    flex-direction: column;
    align-items: center;
    justify-content: center;
    font-family: "Patrick Hand", cursive;
    color: var(--bio-green);
    line-height: 1;
    transform: rotate(-12deg);
  }
  .organic-stamp .stamp-percent { font-size: 16px; }
  .organic-stamp .stamp-word { font-size: 24px; }
  .organic-stamp .stamp-quality { font-size: 14px; }
</style>
</head>
<body>
  <main class="can-label">
    <p class="brand-name">TEKORA</p>
    <h1 class="product-bio">Bio</h1>
    <p class="product-name">Macadamia</p>
    <p class="product-type">NUTS</p>
    <div class="nut-photo" role="img" aria-label="Photo of cracked and whole macadamia nuts with green leaves"></div>
    <p class="origin-note">FROM KENYA</p>
    <ul class="benefit-list">
      <li class="accent">Particularly valuable.</li>
      <li>Best ingredients.</li>
      <li class="accent">Healthy enjoyment.</li>
      <li>Versatile.</li>
    </ul>
    <div class="organic-stamp">
      <span class="stamp-percent">100%</span>
      <span class="stamp-word">Organic</span>
      <span class="stamp-quality">quality</span>
    </div>
  </main>
</body>
</html>
```